Corporate Design + Logo Re-Launch Nordisches Elternschutzkreis
Zielgruppe
Das Nordischen Elternschutzkreis (NEKV) ist ein eingetragener Verein, der im Jahre 1982 gegründet wurde.
Das Nordische Elternschutzkreis eV ist den Rechten der Familie, insbesondere den Kindern verpflichtet. Von Anfang an unterhielt das nordische Elternschutzkreis eine Beratungsstelle in Stuttgart und entwickelte aus seiner jahrelangen betriebenen Tätigkeit ein eigenes Modell, das sogenannte Wendelsteiner Modell. In der zahlreichen familienrechtlichen Tagungen und in Zusammenarbeit mit der Lutherischen Tagungshaus Kirchwald, dem Bundesweiten Sorgerechtskongress wurden auf zahlreichen weiteren Tagungen die Forderungen des NEKV über eine eigenständige Vertretung des Kindes in familiengerichtlichen Verfahren schließlich durch die Erschaffung eines Verfahrensbeistandes Gesetz.
Das Nordische Elternschutzkreis entwickelte diverse Modelle außergerichtlicher Konfliktlösungen, was auch heute noch zentraler Bestandteil seiner Arbeit ist.
The Nordic Parental Care Circle (NEKV) is a registered association that was founded in 1982.
The Nordic Parental Care Circle eV is committed to family rights, especially children. From the beginning, the Nordic parental care circle maintained an advice center in Stuttgart and developed its own model from its many years of activity, the so-called Wendelstein model. In numerous family law conferences and in cooperation with the Lutherische Tagungshaus Kirchwald, the National Custody Congress, the NEKV's demands for an independent representation of the child in family court proceedings were finally met at numerous other conferences by the creation of a procedural lawyer.
The Nordic Parental Care Circle developed various models of out-of-court conflict resolution, which is still a central part of its work today.
Aufgabenstellung
Überarbeitung des NEKV-Logos + Erstellung des Corporate Designs
Das Logo symbolisiert das Kind im Mittelpunkt elterlicher und staatlicher Fürsorge. Eine Auffrischung dieses Logos entsprechend dem dynamischen Auftrag und der Aufgabe des NEKV ist dringend notwendig. Nach wie vor sieht sich das NEKV als ein Sachwalter der Interessen des Kindes als eine moderne Institutionen, die nunmehr auf eine fast vierzigjährige Tätigkeit zurückblicken kann.
Revision of the NEKV-Logo + creation of the corporate design
The logo symbolizes the child in the center of parental and state care. It is urgently necessary to refresh this logo in accordance with the dynamic mandate and the task of the NEKV. As before, the NEKV sees itself as an administrator of the interests of the child as a modern institution that can now look back on almost 40 years of activity.

```html
<!DOCTYPE html>
<html lang="de">
<head>
<meta charset="utf-8">
<title>Briefbogen – Nordisches Elternschutzkreis e. V.</title>
<link rel="stylesheet" href="https://fonts.googleapis.com/css2?family=Open+Sans:wght@400;600;700&display=swap">
<style>
  :root {
    --brand-blue: #1e9ddc;
    --brand-pale: #dcedf7;
    --brand-dots: #cfe5f3;
    --signature-tone: #d6e2f2;
    --ink: #3a3a3a;
    --ink-soft: #777;
    --paper: #ffffff;
    --backdrop: #ececec;
  }
  * { box-sizing: border-box; margin: 0; padding: 0; }
  html, body { width: 1116px; height: 1200px; overflow: hidden; }
  body {
    background: var(--backdrop);
    font-family: "Open Sans", Arial, sans-serif;
    color: var(--ink);
  }
  .letterhead {
    position: absolute;
    left: 168px; top: 48px;
    width: 780px; height: 1103px;
    background: var(--paper);
    box-shadow: 0 6px 24px rgba(0,0,0,.12);
    overflow: hidden;
  }
  .top-rule {
    position: absolute; top: 0; right: 0;
    width: 273px; height: 5px;
    background: var(--brand-blue);
  }
  .brand {
    position: absolute; left: 78px; top: 76px;
    display: flex; align-items: center; gap: 12px;
  }
  .brand-dot {
    width: 44px; height: 44px; border-radius: 50%;
    background: var(--brand-blue);
  }
  .brand-name {
    font-size: 15px; line-height: 17px; font-weight: 400;
    color: var(--ink); text-transform: uppercase;
  }
  .contact {
    position: absolute; right: 50px; top: 68px;
    text-align: right; font-size: 10.5px; line-height: 16px;
    font-style: normal; color: var(--ink);
  }
  .contact strong { font-weight: 700; }
  .contact .office { margin-top: 12px; }
  .sender-line {
    position: absolute; left: 78px; top: 182px;
    font-size: 7.5px; color: var(--ink-soft);
  }
  .fold-mark {
    position: absolute; left: 0; width: 12px; height: 1px;
    background: #bbb;
  }
  .letter-body {
    position: absolute; left: 78px; top: 410px;
    width: 530px; font-size: 12.5px; line-height: 19px;
  }
  .letter-body p { margin-bottom: 14px; }
  .letter-body .closing { margin-top: 28px; margin-bottom: 4px; }
  .letter-body .signer { margin-bottom: 0; }
  .signature {
    display: block; width: 88px; height: 30px;
    margin: 0 0 4px;
  }
  .dot-field {
    position: absolute; left: 646px; top: 850px;
    width: 86px; height: 120px;
  }
  .bank {
    position: absolute; right: 50px; top: 1010px;
    text-align: right; font-size: 9px; line-height: 14px;
    color: var(--ink);
  }
  .deco-circle {
    position: absolute; left: 0; top: 960px;
    width: 306px; height: 306px; border-radius: 50%;
    background: var(--brand-pale);
  }
</style>
</head>
<body>
  <main class="letterhead">
    <div class="top-rule"></div>

    <div class="brand">
      <span class="brand-dot"></span>
      <span class="brand-name">Nordisches<br>Elternschutzkreis<br>e. V.</span>
    </div>

    <address class="contact">
      <strong>Nordisches<br>Elternschutzkreis e. V.</strong><br>
      Lindenweg 48<br>
      70469 Stuttgart<br>
      Tel. +49 711 5550142<br>
      Fax 0711 5550143<br>
      info@elternschutzkreis.example<br>
      www.elternschutzkreis.example
      <div class="office"><strong>BERATUNGSSTELLE</strong><br>Tel. +49 711 5550199</div>
    </address>

    <div class="sender-line">Nordisches Elternschutzkreis e. V. | Lindenweg 48 | 70469 Stuttgart</div>

    <span class="fold-mark" style="top:368px"></span>
    <span class="fold-mark" style="top:551px"></span>

    <section class="letter-body">
      <p>Sehr geehrter Herr John Doe,</p>
      <p>Sed ut perspiciatis unde omnis iste natus error sit voluptatem accusantium doloremque laudantium, totam rem aperiam, eaque ipsa quae ab illo inventore veritatis et quasi architecto beatae vitae dicta sunt explicabo.</p>
      <p>Nemo enim ipsam voluptatem quia voluptas sit aspernatur aut odit aut fugit, sed quia consequuntur magni dolores eos qui ratione voluptatem sequi nesciunt. Neque porro quisquam est, qui dolorem ipsum quia dolor sit amet, consectetur, adipisci velit, sed quia non numquam eius modi tempora incidunt ut labore et dolore magnam aliquam quaerat voluptatem.</p>
      <p>Ut enim ad minima veniam, quis nostrum exercitationem ullam corporis suscipit laboriosam, nisi ut aliquid ex ea commodi consequatur? Quis autem vel eum iure reprehenderit qui in ea voluptate velit esse quam nihil molestiae consequatur, vel illum qui dolorem eum fugiat quo voluptas nulla pariatur?</p>
      <p class="closing">Mit freundlichen Grüßen</p>
      <svg class="signature" role="img" aria-label="Handschriftliche Unterschrift" viewBox="0 0 88 30">
        <rect width="88" height="30" rx="4" fill="var(--signature-tone)"/>
      </svg>
      <p class="signer">Jonas Beispielmann</p>
    </section>

    <svg class="dot-field" role="img" aria-label="Dekoratives Punktmuster" viewBox="0 0 86 120">
      <rect width="86" height="120" rx="8" fill="var(--brand-dots)"/>
    </svg>

    <div class="bank">
      Bankverbindung<br>
      IBAN DE 12 3456 7890 0000<br>
      BIC: NFXXXXXX
    </div>

    <div class="deco-circle"></div>
  </main>
</body>
</html>
```